Business Card Design for Logistics Startup

Link to my logo source file -
https://www.fylvault.com/sh/qormx7pl2vkc8wd/KLmrT9_ZPq4BnWvHhYtaeCxo?dl=0

We want a statement in our business card!
I have go thru your portfolio, and invites 3 of you guys to design my business card as the previous designer cannot give me the feel.
Let me know if you want any information.
Thanks.
Updates

Target Market(s)

Transport and Logistics
: Shippers, Freight Forwarders and Carriers.

Industry/Entity Type

Business

Contact Information for Business Card

Our details;

Name: Marcus Loh
Designation: General Manager
Mobile: +65 91234508
Email: marcus.loh@corvinmarl.com
Address: 7 Lorong Pelita Rise
RHOMB Tower #09-17
Singapore 639217

Name: Victor Yeo
Designation: Director
Mobile: +65 93416672
Email: victor.yeo@corvinmarl.com
RHOMB Tower #09-17
Singapore 639217

Colors
f37122

Requirements
Must have
• Logo from my source file.
• Please included tagline: Transport and Logistics
• If you guy can think of a tagline - Using E and S, that will be perfect. Such as Excellence in Service..

```html
<!DOCTYPE html>
<html lang="en">
<head>
<meta charset="utf-8">
<title>Corvin Marl – Business Card</title>
<link rel="stylesheet" href="https://fonts.googleapis.com/css2?family=Raleway:wght@400;500;600&display=swap">
<style>
  :root {
    --brand-orange: #f39a2c;
    --brand-orange-deep: #f08a1e;
    --brand-orange-light: #f5b256;
    --card-white: #ffffff;
    --backdrop: #e9e6e1;
    --card-shadow: rgba(60, 40, 20, 0.22);
  }
  * { box-sizing: border-box; margin: 0; padding: 0; }
  html, body {
    width: 1200px; height: 1000px; overflow: hidden;
    background: var(--backdrop);
    font-family: "Raleway", "Helvetica Neue", Arial, sans-serif;
  }
  .stage {
    position: relative; width: 1200px; height: 1000px;
  }
  .card {
    position: absolute; left: 250px; width: 700px; height: 400px;
    box-shadow: 0 10px 28px var(--card-shadow);
    overflow: hidden;
  }
  /* Back side */
  .card--back {
    top: 60px;
    background: linear-gradient(100deg, var(--brand-orange-deep) 0%, var(--brand-orange) 55%, var(--brand-orange-light) 100%);
    color: var(--card-white);
  }
  .card--back .tagline-es {
    position: absolute; left: 250px; top: 150px;
    font-size: 19px; font-weight: 400; letter-spacing: 0.5px;
  }
  .card--back .brand {
    position: absolute; right: 40px; top: 215px; text-align: center;
  }
  /* Brand lockup */
  .brand-name {
    font-weight: 500; font-size: 30px; letter-spacing: 3px; line-height: 1;
  }
  .brand-tagline {
    font-weight: 500; font-size: 11px; letter-spacing: 2.4px; margin-top: 6px;
  }
  /* Front side */
  .card--front {
    top: 530px; background: var(--card-white); color: var(--brand-orange);
  }
  .card--front .brand {
    position: absolute; left: 0; right: 0; top: 120px; text-align: center;
  }
  .card--front .brand-name { font-size: 36px; }
  .card--front .brand-tagline { font-size: 12px; }
  .name-band {
    position: absolute; left: 0; top: 248px; width: 340px; height: 78px;
    background: var(--brand-orange); color: var(--card-white);
    padding: 12px 0 0 70px;
  }
  .person-name { font-size: 34px; font-weight: 500; letter-spacing: 4px; line-height: 1; }
  .person-title { font-size: 15px; font-weight: 400; letter-spacing: 2.5px; margin-top: 7px; }
  .contact-list {
    position: absolute; left: 385px; top: 220px; list-style: none;
  }
  .contact-item {
    display: flex; align-items: center; gap: 16px;
    font-size: 20px; font-weight: 500; height: 38px;
  }
  .contact-icon { width: 22px; height: 22px; flex: none; }
  .address {
    position: absolute; left: 70px; top: 350px;
    font-size: 19px; font-weight: 500; letter-spacing: 0.3px;
  }
</style>
</head>
<body>
<main class="stage">
  <section class="card card--back" aria-label="Card back">
    <p class="tagline-es">Excellence in Service..</p>
    <div class="brand">
      <div class="brand-name">CORVIN MARL</div>
      <div class="brand-tagline">TRANSPORT AND LOGISTICS</div>
    </div>
  </section>

  <section class="card card--front" aria-label="Card front">
    <div class="brand">
      <div class="brand-name">CORVIN MARL</div>
      <div class="brand-tagline">TRANSPORT AND LOGISTICS</div>
    </div>

    <div class="name-band">
      <div class="person-name">MARCUS LOH</div>
      <div class="person-title">GENERAL MANAGER</div>
    </div>

    <ul class="contact-list">
      <li class="contact-item">
        <svg class="contact-icon" viewBox="0 0 22 22" aria-hidden="true">
          <rect x="5" y="1.5" width="12" height="19" rx="2" fill="none" stroke="currentColor" stroke-width="1.6"/>
          <line x1="5" y1="16" x2="17" y2="16" stroke="currentColor" stroke-width="1.4"/>
          <circle cx="11" cy="18.2" r="0.9" fill="currentColor"/>
        </svg>
        <span>+65 91234508</span>
      </li>
      <li class="contact-item">
        <svg class="contact-icon" viewBox="0 0 22 22" aria-hidden="true">
          <rect x="1.5" y="5" width="19" height="13" fill="currentColor"/>
          <polyline points="1.5,5 11,12.5 20.5,5" fill="none" stroke="#ffffff" stroke-width="1.4"/>
        </svg>
        <span>marcus.loh@corvinmarl.com</span>
      </li>
    </ul>

    <p class="address">7 Lorong Pelita Rise, RHOMB Tower #09-17, Singapore 639217</p>
  </section>
</main>
</body>
</html>
```